Cardiology practice business card

We need a business card for our cardiology practice "Bellmoor Cardiology". We have a new logo, attached below. We like the colours in the logo - red and charcoal. The front of the business card will need to have the doctors name, address, phone number and email. The back will need to have space to write 2 appointment dates and times.

```html
<!DOCTYPE html>
<html lang="en">
<head>
<meta charset="utf-8">
<title>Bellmoor Cardiology – Business Card</title>
<link href="https://fonts.googleapis.com/css2?family=Roboto:wght@400;700;900&display=swap" rel="stylesheet">
<style>
  :root {
    --stage: #cccccc;
    --label: #5f6062;
    --paper: #ffffff;
    --red-deep: #a80000;
    --red-mid: #b8272a;
    --red-name: #8b1a1a;
    --charcoal: #3d3e42;
    --mist: #e6e7e8;
    --blush: #f5e1e2;
    --ink: #333333;
    --rule: #666666;
  }
  * { margin: 0; padding: 0; box-sizing: border-box; }
  html, body {
    width: 1200px; height: 1112px; overflow: hidden;
    background: var(--stage);
    font-family: "Roboto", Arial, sans-serif;
  }
  .stage { position: relative; width: 1200px; height: 1112px; }
  .side-label {
    position: absolute;
    font-weight: 900; font-size: 28px; letter-spacing: 0.5px;
    color: var(--label);
  }
  .side-label--front { left: 74px; top: 40px; }
  .side-label--back { left: 371px; top: 559px; }
  .card {
    position: absolute; width: 753px; height: 443px;
    background: var(--paper); overflow: hidden;
  }
  .card--front { left: 75px; top: 75px; }
  .card--back { left: 372px; top: 594px; }
  .card__waves { position: absolute; inset: 0; width: 100%; height: 100%; }
  .brand-name {
    position: absolute; color: var(--red-deep);
    font-weight: 700; white-space: nowrap;
  }
  .card--front .brand-name {
    left: 0; right: 0; top: 158px; text-align: center;
    font-size: 46px; letter-spacing: 1px;
  }
  .card--back .brand-name {
    right: 44px; top: 66px; font-size: 20px; letter-spacing: 0.5px;
  }
  .holder { position: absolute; left: 44px; top: 57px; }
  .holder__name { font-size: 21px; font-weight: 700; color: var(--red-name); line-height: 1.2; }
  .holder__title { font-size: 16.5px; color: var(--ink); line-height: 1.3; }
  .divider {
    position: absolute; left: 44px; top: 214px; width: 664px; height: 10px;
  }
  .divider__line { position: absolute; left: 0; right: 0; top: 4px; height: 2px; background: var(--rule); }
  .divider__accent { position: absolute; left: 0; top: 0; width: 244px; height: 10px; background: var(--red-name); }
  .contact {
    position: absolute; display: flex; align-items: center; gap: 12px;
    font-size: 20.5px; color: var(--ink);
  }
  .contact svg { width: 22px; height: 22px; flex: none; }
  .contact--phone { left: 44px; top: 249px; }
  .contact--email { left: 44px; top: 287px; }
  .contact--handle { left: 377px; top: 249px; }
  .contact--address { left: 377px; top: 287px; }
</style>
</head>
<body>
<main class="stage">
  <h2 class="side-label side-label--front">FRONT</h2>
  <section class="card card--front">
    <svg class="card__waves" viewBox="0 0 1004 591" preserveAspectRatio="none" aria-hidden="true">
      <path d="M0,420 Q150,500 330,540 L330,591 L0,591 Z" fill="var(--mist)"/>
      <path d="M0,512 L210,591 L0,591 Z" fill="var(--charcoal)"/>
      <path d="M160,522 C420,575 720,540 1004,350 L1004,591 L230,591 Z" fill="var(--red-deep)"/>
      <path d="M160,522 Q270,552 390,591 L230,591 Z" fill="var(--red-mid)"/>
      <path d="M960,591 L1004,565 L1004,591 Z" fill="var(--red-mid)"/>
    </svg>
    <p class="brand-name">Bellmoor Cardiology</p>
  </section>

  <h2 class="side-label side-label--back">BACK</h2>
  <section class="card card--back">
    <svg class="card__waves" viewBox="0 0 1004 591" preserveAspectRatio="none" aria-hidden="true">
      <path d="M0,435 Q120,500 270,591 L0,591 Z" fill="var(--blush)"/>
      <path d="M0,530 L150,591 L0,591 Z" fill="var(--red-deep)"/>
      <path d="M190,552 C450,600 750,540 1004,398 L1004,591 L230,591 Z" fill="var(--red-deep)"/>
    </svg>
    <p class="brand-name">Bellmoor Cardiology</p>
    <div class="holder">
      <p class="holder__name">Your Name</p>
      <p class="holder__title">Head of Cardiology</p>
    </div>
    <div class="divider"><span class="divider__line"></span><span class="divider__accent"></span></div>

    <p class="contact contact--phone">
      <svg viewBox="0 0 24 24" aria-hidden="true"><circle cx="12" cy="12" r="12" fill="var(--red-deep)"/><path d="M8.5,6.5 l2,0 l1,3 l-1.5,1 a7,7 0 0 0 3.5,3.5 l1,-1.5 l3,1 l0,2 a1.5,1.5 0 0 1 -1.5,1.5 a9,9 0 0 1 -9,-9 a1.5,1.5 0 0 1 1.5,-1.5 Z" fill="#fff"/></svg>
      +123-456-7890
    </p>
    <p class="contact contact--email">
      <svg viewBox="0 0 24 24" aria-hidden="true"><circle cx="12" cy="12" r="12" fill="var(--red-deep)"/><rect x="6" y="8" width="12" height="8" fill="none" stroke="#fff" stroke-width="1.4"/><path d="M6,8 L12,13 L18,8" fill="none" stroke="#fff" stroke-width="1.4"/></svg>
      hello@youremail.com
    </p>
    <p class="contact contact--handle">
      <svg viewBox="0 0 24 24" aria-hidden="true"><circle cx="12" cy="12" r="12" fill="var(--red-deep)"/><circle cx="12" cy="9.5" r="3" fill="#fff"/><path d="M7,17.5 a5,4.5 0 0 1 10,0 Z" fill="#fff"/></svg>
      @yourname
    </p>
    <p class="contact contact--address">
      <svg viewBox="0 0 24 24" aria-hidden="true"><circle cx="12" cy="12" r="12" fill="var(--red-deep)"/><path d="M12,19 C8,14 7.5,12 7.5,10.5 a4.5,4.5 0 0 1 9,0 C16.5,12 16,14 12,19 Z" fill="#fff"/><circle cx="12" cy="10.5" r="1.6" fill="var(--red-deep)"/></svg>
      123 Anywhere St., Any City
    </p>
  </section>
</main>
</body>
</html>
```